VELMAR Industries PP Presentation

I would a much more professional looking and acting ppp. We provide solar powered pumping systems to the oil and gas sector. I would like it to pop so to say, so you wont want to look away. much better flow and continuity.
please follow all of our branding colors and schemes.
is it possible for it to be emailable?

Target Market(s)

oil and gas sectors around the world

Industry/Entity Type

Oil And Gas

Requirements
Must have
• pizzazz,
Nice to have
• some movement in the presentation

```html
<!DOCTYPE html>
<html lang="en">
<head>
<meta charset="utf-8">
<title>VELMAR Industries – Presentation Overview</title>
<link href="https://fonts.googleapis.com/css2?family=Montserrat:wght@400;500;700;800;900&display=swap" rel="stylesheet">
<style>
  :root{
    --canvas:#d6d7d9;
    --paper:#ffffff;
    --band:#58585a;
    --ink:#231f20;
    --grey:#8a8a8c;
    --lime:#a6ce39;
    --green:#1aab4b;
    --forest:#0d7a4a;
    --teal:#1a9e78;
    --yellow:#fdb913;
    --night:#231f20;
  }
  *{box-sizing:border-box;margin:0;padding:0}
  html,body{width:1105px;height:1200px;overflow:hidden}
  body{background:var(--canvas);font-family:"Montserrat",sans-serif;color:var(--ink);position:relative}
  .slide{position:absolute;width:838px;height:522px;background:var(--paper);overflow:hidden;transform:scale(.598);transform-origin:0 0}
  .slide--dark{background:var(--night)}
  .slide > *{position:absolute}
  .title-band{left:0;top:23px;width:838px;height:46px;background:var(--band)}
  .title-band::before{content:"";position:absolute;left:0;top:0;width:13px;height:46px;background:var(--lime)}
  .title-band::after{content:"";position:absolute;left:13px;top:0;width:12px;height:46px;background:var(--forest)}
  .slide-title{left:48px;top:23px;height:46px;line-height:46px;font-weight:900;font-size:33px;color:#fff;white-space:nowrap}
  .slide-title .lead-yellow{color:var(--yellow)}
  .slide-title .lead-green{color:var(--green)}
  .slide-title .tagline{font-weight:500;font-size:23px}
  .slide-title--compact{font-size:29px}
  .slide-title--compact .tagline{font-size:19px}
  .brand{left:36px;top:470px;display:flex;align-items:center;gap:6px;font-weight:800;font-size:20px;color:var(--ink)}
  .slide--dark .brand{color:#fff}
  .brand-dot{width:16px;height:16px;border-radius:50%;background:var(--green)}
  .page-no{left:777px;top:492px;font-size:9px;color:var(--ink);display:flex;align-items:center;gap:2px}
  .slide--dark .page-no{color:#fff}
  .page-no i{width:0;height:0;border-top:4px solid transparent;border-bottom:4px solid transparent}
  .page-no .prev{border-right:6px solid var(--green)}
  .page-no .next{border-left:6px solid var(--green)}
  .list{list-style:none;font-size:12px;line-height:1.2}
  .list li{position:relative}
  .arrow-item{padding-left:13px;margin-bottom:4px}
  .arrow-item::before{content:"";position:absolute;left:0;top:3px;border-top:4px solid transparent;border-bottom:4px solid transparent;border-left:7px solid var(--green)}
  .dot-item{padding-left:27px;margin-bottom:5px}
  .dot-item::before{content:"";position:absolute;left:14px;top:5px;width:5px;height:5px;border-radius:50%;background:var(--green)}
  .small-head{font-size:12.5px;padding-left:13px}
  .small-head::before{content:"";position:absolute;left:0;top:3px;border-top:4px solid transparent;border-bottom:4px solid transparent;border-left:7px solid var(--green)}
  .client{font-weight:700;color:var(--grey);font-size:17px;white-space:nowrap}
  .lede{font-size:22px;font-weight:500}
  .green-lede{font-size:18.5px;line-height:24px;color:var(--green);font-weight:500}
  .body-note{font-size:12.5px;line-height:16px}
  .body-note b{color:var(--green);font-weight:700}
  .pie-label{color:#fff;text-align:center;font-size:14px;line-height:18px;transform:translateX(-50%);white-space:nowrap}
  .pie-label strong{display:block;font-weight:900;font-size:30px;line-height:32px}
  .pie-label strong small{font-size:17px}
  .gas-badge{display:flex;align-items:center;justify-content:center;color:#fff;font-weight:900;font-size:32px;border-radius:50px;background:var(--lime)}
  .gas-badge sub{font-size:14px;vertical-align:baseline;margin-top:14px}
  .option-disc{border-radius:50%;display:flex;align-items:center;justify-content:center;text-align:center;color:#fff;font-weight:900;font-size:28px;line-height:32px}
  .option-disc--self{background:var(--yellow)}
  .option-disc--fin{background:var(--green)}
  .col-head{font-weight:800;font-size:15px}
  .col-list{font-size:13px;line-height:16px;width:360px}
  .col-list li{padding-left:14px;margin-bottom:7px;position:relative;list-style:none}
  .col-list li::before{content:"";position:absolute;left:0;top:5px;width:5px;height:5px;border-radius:50%;background:var(--green)}
  .fine-green{font-size:13px;font-weight:700;color:var(--green);line-height:16px}
  .step-text{color:#fff;font-size:20px;line-height:22px;text-align:center;transform:translateX(-50%);width:190px}
  .placeholder{border-radius:6px}
</style>
</head>
<body>

<section class="slide" style="left:40px;top:56px">
  <div class="title-band"></div>
  <h2 class="slide-title">The Velmar Advantage</h2>
  <ul class="list" style="left:70px;top:111px;width:275px">
    <li class="arrow-item">Proven Track Record:</li>
    <li class="dot-item">3000+ pumps installed to date</li>
    <li class="dot-item">Solar chemical Injection pump systems</li>
    <li class="dot-item">9 years in operation</li>
    <li class="dot-item">Equipment deployed throughout Western Canada and the USA</li>
    <li class="arrow-item">Only system to deliver verifiable carbon credits over multiple collection platforms</li>
  </ul>
  <p class="small-head" style="left:390px;top:110px">Current Velmar Customers Include</p>
  <span class="client" style="left:400px;top:155px">Brenwick</span>
  <span class="client" style="left:520px;top:155px">Northfell</span>
  <span class="client" style="left:680px;top:155px">Corvane</span>
  <span class="client" style="left:388px;top:205px">Halden</span>
  <span class="client" style="left:535px;top:205px">Prairie Basin</span>
  <span class="client" style="left:660px;top:205px">Kestrel Resources</span>
  <p class="small-head" style="left:393px;top:246px">Velmar Pump Development</p>
  <svg style="left:370px;top:272px" width="420" height="200" viewBox="370 272 420 200" role="img" aria-label="Area chart of pumps deployed per year and cumulative pumps, 2009 to 2019">
    <g stroke="#e3e3e3" stroke-width="1">
      <line x1="412" y1="280" x2="772" y2="280"/><line x1="412" y1="296.5" x2="772" y2="296.5"/>
      <line x1="412" y1="313" x2="772" y2="313"/><line x1="412" y1="329.5" x2="772" y2="329.5"/>
      <line x1="412" y1="346" x2="772" y2="346"/><line x1="412" y1="362.5" x2="772" y2="362.5"/>
      <line x1="412" y1="379" x2="772" y2="379"/><line x1="412" y1="395.5" x2="772" y2="395.5"/>
      <line x1="412" y1="412" x2="772" y2="412"/><line x1="412" y1="429" x2="772" y2="429"/>
    </g>
    <polygon fill="#8dc63f" points="412,429 448,427.3 484,424 520,420.7 556,410.8 592,397.6 628,389.3 664,392.6 700,352.9 736,339.6 772,303.2 772,429"/>
    <polygon fill="var(--teal)" points="412,429 448,428.3 484,427.3 520,425.7 556,422.4 592,417.4 628,419.1 664,424 700,407.5 736,410.8 772,402.5 772,429"/>
    <g font-family="Montserrat,sans-serif" font-size="6.5" fill="#555" text-anchor="end">
      <text x="404" y="282">4500</text><text x="404" y="298">4000</text><text x="404" y="315">3500</text>
      <text x="404" y="331">3000</text><text x="404" y="348">2500</text><text x="404" y="364">2000</text>
      <text x="404" y="381">1500</text><text x="404" y="397">1000</text><text x="404" y="414">500</text><text x="404" y="431">0</text>
    </g>
    <g font-family="Montserrat,sans-serif" font-size="6.5" fill="#555" text-anchor="middle">
      <text x="412" y="442">2009</text><text x="448" y="442">2010</text><text x="484" y="442">2011</text>
      <text x="520" y="442">2012</text><text x="556" y="442">2013</text><text x="592" y="442">2014</text>
      <text x="628" y="442">2015</text><text x="664" y="442">2016</text><text x="700" y="442">2017</text>
      <text x="736" y="442">2018</text><text x="772" y="442">2019</text>
    </g>
    <g font-family="Montserrat,sans-serif" font-size="6" fill="#555">
      <rect x="490" y="451" width="4" height="4" fill="var(--teal)"/><text x="496" y="455">Pumps Deployed per year</text>
      <rect x="588" y="451" width="4" height="4" fill="#8dc63f"/><text x="594" y="455">Cumulative Pumps Deployed</text>
    </g>
  </svg>
  <div class="brand"><span class="brand-dot"></span>VELMAR</div>
  <div class="page-no"><i class="prev"></i>01<i class="next"></i></div>
</section>

<section class="slide" style="left:563px;top:56px">
  <div class="title-band"></div>
  <h2 class="slide-title">Why Methane?</h2>
  <p class="green-lede" style="left:61px;top:107px;width:260px">Methane (CH4) has a Global Warming Potential (GWP) more than <b style="font-weight:800">25 times</b> carbon dioxide (CO2)</p>
  <div class="gas-badge" role="img" aria-label="Illustration of a green gas cloud with rising bubbles" style="left:324px;top:135px;width:146px;height:92px">CH<sub>4</sub></div>
  <p class="body-note" style="left:61px;top:238px;width:340px">Alberta’s Climate Leadership plans to <b>reduce methane emissions</b> from upstream oil and gas operations by <b>45%</b> before 2025</p>
  <p class="body-note" style="left:61px;top:306px">1 Ton of conserved methane ⟶ 25 Tons CO2e</p>
  <p class="green-lede" style="left:61px;top:336px;width:385px">Replacement of Pneumatic devices is one of the lowest cost options on a per tonne of CO2e basis 160,000 pneumatic pumps are currently installed</p>
  <svg style="left:470px;top:110px" width="360" height="350" viewBox="470 110 360 350" role="img" aria-label="Pie chart of methane emission sources">
    <g stroke="#fff" stroke-width="6" stroke-linejoin="round">
      <path d="M648,285 L648,120 A165,165 0 0 1 787.3,373.4 Z" fill="var(--lime)"/>
      <path d="M648,285 L787.3,373.4 A165,165 0 0 1 577.7,434.3 Z" fill="var(--grey)"/>
      <path d="M648,285 L577.7,434.3 A165,165 0 0 1 508.7,373.4 Z" fill="var(--band)"/>
      <path d="M648,285 L508.7,373.4 A165,165 0 0 1 520.9,179.8 Z" fill="var(--green)"/>
      <path d="M648,285 L520.9,179.8 A165,165 0 0 1 648,120 Z" fill="var(--forest)"/>
    </g>
  </svg>
  <p class="pie-label" style="left:713px;top:212px"><strong>34<small>%</small></strong>Leaks</p>
  <p class="pie-label" style="left:671px;top:342px"><strong>23<small>%</small></strong>General Venting</p>
  <p class="pie-label" style="left:556px;top:362px"><strong>9<small>%</small></strong></p>
  <p class="pie-label" style="left:499px;top:404px;color:var(--band)">Compresssor<br>Emissions</p>
  <p class="pie-label" style="left:526px;top:232px"><strong>20<small>%</small></strong>Pneumatic<br>Emissions</p>
  <p class="pie-label" style="left:597px;top:150px"><strong>14<small>%</small></strong>Other</p>
  <p style="left:424px;top:467px;font-size:8px">National Climate Office. Proposed Methane Regulations Webinar: 2017</p>
  <div class="brand"><span class="brand-dot"></span>VELMAR</div>
  <div class="page-no"><i class="prev"></i>01<i class="next"></i></div>
</section>

<section class="slide" style="left:40px;top:431px">
  <div class="title-band"></div>
  <h2 class="slide-title">What are your options?</h2>
  <p class="lede" style="left:54px;top:98px">Everyone has a different need and fit</p>
  <div class="placeholder" role="img" aria-label="Outline icon of an open hand holding dollar coins" style="left:100px;top:215px;width:165px;height:150px;background:linear-gradient(135deg,#e6e6e7,#cfcfd1)"></div>
  <div class="option-disc option-disc--self" style="left:324px;top:200px;width:176px;height:176px">Self<br>Finance</div>
  <div class="option-disc option-disc--fin" style="left:570px;top:200px;width:176px;height:176px">Velmar<br>Financing</div>
  <div class="brand"><span class="brand-dot"></span>VELMAR</div>
  <div class="page-no"><i class="prev"></i>01<i class="next"></i></div>
</section>

<section class="slide" style="left:565px;top:432px">
  <div class="title-band"></div>
  <h2 class="slide-title"><span class="lead-yellow">Self Financing</span> <span class="tagline">– Great if you have capital to Deploy</span></h2>
  <p class="lede" style="left:54px;top:100px">How can Velmar Carbon help you with this?</p>
  <ul class="list" style="left:54px;top:142px;width:700px;font-size:12.5px;line-height:1.25">
    <li class="arrow-item" style="padding-left:22px">Velmar Carbon can manage your carbon credit program for you this includes:</li>
    <li class="dot-item" style="padding-left:39px;margin-bottom:7px">Registering the locations and equipment in one of Velmar’s Alberta Emissions Offset Registries</li>
    <li class="dot-item" style="padding-left:39px;margin-bottom:7px">Gathering the required documentation and pictures to ensure credits can be audited successfully</li>
    <li class="dot-item" style="padding-left:39px;margin-bottom:7px">Gather data and process when it comes time to generate the credits</li>
    <li class="dot-item" style="padding-left:39px;margin-bottom:7px">Process, audit and verify the credits</li>
    <li class="dot-item" style="padding-left:39px;margin-bottom:28px">Market the credits so that you receive top dollar.</li>
    <li class="arrow-item" style="padding-left:22px">Velmar takes a percentage of the credits, no hidden fees or costs. We get paid when you are successful and get paid.</li>
  </ul>
  <div class="brand"><span class="brand-dot"></span>VELMAR</div>
  <div class="page-no"><i class="prev"></i>01<i class="next"></i></div>
</section>

<section class="slide" style="left:40px;top:799px">
  <div class="title-band"></div>
  <h2 class="slide-title slide-title--compact"><span class="lead-green">Velmar Financing</span> <span class="tagline">– Save your capital but still get compliant</span></h2>
  <p class="lede" style="left:54px;top:92px">Velmar Financing Options:</p>
  <svg style="left:161px;top:126px" width="68" height="68" viewBox="0 0 68 68" aria-hidden="true">
    <circle cx="34" cy="34" r="34" fill="var(--green)"/>
    <circle cx="34" cy="34" r="21" fill="none" stroke="#fff" stroke-width="3"/>
    <line x1="34" y1="36" x2="34" y2="18" stroke="#fff" stroke-width="3" stroke-linecap="round"/>
    <circle cx="34" cy="38" r="4" fill="#fff"/>
  </svg>
  <svg style="left:562px;top:126px" width="68" height="68" viewBox="0 0 68 68" aria-hidden="true">
    <circle cx="34" cy="34" r="34" fill="var(--green)"/>
    <rect x="24" y="22" width="24" height="22" rx="3" fill="#fff"/>
    <circle cx="20" cy="40" r="7" fill="none" stroke="#fff" stroke-width="3"/>
    <rect x="50" y="16" width="3" height="18" fill="#fff"/>
  </svg>
  <p class="col-head" style="left:54px;top:202px">High to Low Bleed change outs:</p>
  <ul class="col-list" style="left:54px;top:224px">
    <li>The program in most cases finances the cost of removal and replacement of the equipment</li>
    <li>Payout times can be under a year.</li>
    <li>The Producer’s percentage initially is used to pay down the capital costs</li>
    <li>Once the project reaches payout the Producer receives their portion of the revenue</li>
  </ul>
  <p class="col-head" style="left:442px;top:202px">Pump &amp; Compressor change outs:</p>
  <ul class="col-list" style="left:442px;top:224px">
    <li>Again the program can finance all of the equipment costs and some of the installation or all of the installation costs</li>
    <li>Payout times can be one to two years.</li>
    <li>The Producer’s percentage initially is used to pay down the capital costs</li>
    <li>Once the project reaches payout the Producer receives their portion of the revenue</li>
  </ul>
  <p class="fine-green" style="left:57px;top:403px;width:720px">In either case if the project doesn’t get to payout the producer only owes the balance outstanding there are no additional charges.</p>
  <div class="brand"><span class="brand-dot"></span>VELMAR</div>
  <div class="page-no"><i class="prev"></i>01<i class="next"></i></div>
</section>

<section class="slide slide--dark" style="left:564px;top:800px">
  <div role="img" aria-label="Dark photograph of an oil pump jack silhouetted at an oil field" style="left:0;top:0;width:838px;height:522px;background:radial-gradient(ellipse at 65% 35%,#3a3637 0%,#262223 55%,#161314 100%)"></div>
  <div class="title-band"></div>
  <h2 class="slide-title">What’s next?</h2>
  <div class="placeholder" role="img" aria-label="White line icon of a magnifying glass with location pin beside a pump jack" style="left:86px;top:178px;width:176px;height:128px;background:rgba(255,255,255,.14)"></div>
  <div class="placeholder" role="img" aria-label="White line icon of hands placing a sprouting plant" style="left:368px;top:186px;width:112px;height:120px;background:rgba(255,255,255,.14)"></div>
  <div class="placeholder" role="img" aria-label="White line icon of a fuel pump with a green drop" style="left:630px;top:196px;width:98px;height:108px;background:rgba(255,255,255,.14)"></div>
  <p class="step-text" style="left:176px;top:318px">Identify suitable well sites</p>
  <p class="step-text" style="left:424px;top:318px">Lease equipment to reduce emissions</p>
  <p class="step-text" style="left:674px;top:318px">Conserve fuel gas and generate offset credits</p>
  <div class="brand"><span class="brand-dot"></span>VELMAR</div>
  <div class="page-no"><i class="prev"></i>01<i class="next"></i></div>
</section>

</body>
</html>
```